Landing Page IT Security Vendor

We need a landing page that uses our colour scheme (www.veldonguard.com). We created a draft (see attached). We do not need standard stock template design pages. Please only apply if you can design pages from scratch and try to be as close as possible to our draft. It is ok to also purchase commecrial stock pictures

Coding

Coded - Design and coding required

Number of Pages Required

1 page

```html
<!DOCTYPE html>
<html lang="en">
<head>
<meta charset="utf-8">
<title>Veldon Guard – Security Awareness Training</title>
<link href="https://fonts.googleapis.com/css2?family=Montserrat:wght@400;500;700;800;900&family=Roboto:wght@400;500;700&display=swap" rel="stylesheet">
<style>
:root{
  --teal:#15b3bf;
  --teal-dark:#0fa3b0;
  --panel:#def2f8;
  --heading:#17a6b6;
  --orange:#f9a61e;
  --ink:#1c1c1c;
  --white:#ffffff;
  --illus-a:#5aa6ea;
  --illus-b:#2f5fc4;
}
*{box-sizing:border-box;margin:0;padding:0}
html,body{width:1200px;height:2396px;overflow:hidden}
body{position:relative;font-family:"Roboto",sans-serif;color:var(--ink);background:var(--white)}
.abs{position:absolute}

/* Hero */
.hero{position:absolute;left:0;top:0;width:1200px;height:860px;background:var(--teal)}
.brand{position:absolute;left:34px;top:30px;display:flex;align-items:center;gap:8px}
.brand-dot{width:22px;height:22px;border-radius:50%;background:var(--orange)}
.brand-name{font-family:"Montserrat",sans-serif;font-weight:800;font-size:28px;color:#1b1b1b}
.lang{position:absolute;left:91px;top:86px;color:var(--white);font-family:"Montserrat",sans-serif;font-size:12px;font-weight:500}
.lang::after{content:"";display:inline-block;margin-left:8px;border:4px solid transparent;border-top:5px solid var(--white);vertical-align:-2px}
.nav{position:absolute;right:12px;top:53px;display:flex;gap:12px;align-items:center;font-family:"Montserrat",sans-serif;font-size:15px;color:var(--white)}
.nav a{color:var(--white);text-decoration:none;padding:8px 10px}
.nav .active{background:#5fd2d8;border-radius:18px;padding:8px 14px;color:#e9fbfc}
.nav .drop::after{content:"";display:inline-block;margin-left:4px;width:5px;height:5px;border-right:1.5px solid var(--white);border-bottom:1.5px solid var(--white);transform:rotate(45deg);vertical-align:3px}
.awards{position:absolute;top:145px;left:98px;display:flex;gap:32px;color:var(--white);font-size:11px;line-height:16px;font-family:"Montserrat",sans-serif}
.award{display:flex;gap:10px;align-items:center}
.award svg{flex:none}
.eyebrow{position:absolute;left:47px;top:364px;color:var(--white);font-family:"Montserrat",sans-serif;font-size:19px;font-weight:500;letter-spacing:.3px}
.hero-title{position:absolute;left:47px;top:406px;width:560px;color:var(--white);font-family:"Montserrat",sans-serif;font-weight:900;font-size:31px;line-height:41px;letter-spacing:0;z-index:2}
.demo-btn{position:absolute;left:51px;top:561px;width:253px;height:60px;border-radius:30px;background:#b8e9ec;color:#4b6a6d;font-family:"Montserrat",sans-serif;font-size:19px;letter-spacing:1px;display:flex;align-items:center;justify-content:center}
.hero-illus{position:absolute;left:540px;top:196px;width:623px;height:586px;border-radius:40px;background:radial-gradient(circle at 50% 42%,var(--illus-b) 0 22%,var(--illus-a) 40%,rgba(125,190,245,.35) 70%,rgba(21,179,191,0) 100%)}
.dots{position:absolute;left:1133px;top:374px;display:flex;gap:11px}
.dots span{width:13px;height:13px;border:1.5px solid var(--white);border-radius:50%}

/* Help */
.help{position:absolute;left:99px;top:809px;width:1003px;height:605px;background:var(--panel);box-shadow:0 6px 18px rgba(0,0,0,.08)}
.help h2{position:absolute;top:42px;left:0;width:100%;text-align:center;font-family:"Montserrat",sans-serif;font-weight:800;font-size:39px;color:var(--heading);letter-spacing:.5px}
.card{position:absolute;top:135px;width:284px;height:405px;background:var(--white);box-shadow:0 2px 8px rgba(0,0,0,.12)}
.card h3{position:absolute;left:32px;right:10px;font-family:"Roboto",sans-serif;font-weight:700;font-size:15.5px;line-height:20px;color:var(--orange)}
.card .lead{position:absolute;left:32px;right:8px;font-weight:700;font-size:15px;line-height:20px;color:#111}
.card p.body{position:absolute;left:30px;right:8px;font-size:13.5px;line-height:17px;color:#222}
.card-btn{position:absolute;height:47px;border-radius:5px;background:var(--orange);color:var(--white);font-size:16px;display:flex;align-items:center;justify-content:center}

/* MSSP band */
.mssp{position:absolute;left:0;top:1451px;width:1200px;height:139px;background:var(--teal);display:flex;align-items:center;justify-content:center;color:var(--white);font-family:"Montserrat",sans-serif;font-weight:500;font-size:29px;letter-spacing:.5px}
.mssp a{color:var(--white);margin-left:10px;text-decoration:underline}

/* Trust */
.trust-title{position:absolute;left:142px;top:1667px;font-size:26px;line-height:32px;color:#111}
.trust-title .num{color:var(--orange)}
.trust-copy{position:absolute;left:145px;top:1756px;width:480px;font-size:14px;line-height:18px;color:#111}
.trust-copy p{margin-bottom:18px}
.cta{position:absolute;left:141px;top:1916px;width:486px;height:57px;background:var(--orange);border-radius:5px;color:var(--white);font-weight:700;font-size:14.5px;display:flex;align-items:center;justify-content:center}
.clients{position:absolute;left:721px;top:1660px;width:339px;height:312px;background:var(--white);box-shadow:0 2px 10px rgba(0,0,0,.06)}
.client{position:absolute;font-family:"Montserrat",sans-serif;font-weight:700;font-size:19px;color:#1d3f8f;display:flex;align-items:center;gap:6px}
.client .sq{width:12px;height:12px;background:currentColor}

/* Footer */
.footer{position:absolute;left:0;top:2035px;width:1200px;height:361px;background:var(--teal);color:var(--white);font-family:"Montserrat",sans-serif;font-size:15px;line-height:22px}
.footer .frame{position:absolute;left:32px;top:13px;width:1143px;height:348px;border-left:1px solid rgba(255,255,255,.4);border-right:1px solid rgba(255,255,255,.4)}
.footer h4{font-size:17px;font-weight:500}
.footer .rule{position:absolute;left:32px;top:223px;width:1143px;height:1px;background:rgba(255,255,255,.6)}
.foot-brand{position:absolute;left:36px;top:280px;display:flex;align-items:center;gap:6px}
.foot-brand .brand-dot{width:14px;height:14px}
.foot-brand span.n{font-weight:800;font-size:17px;color:#1b1b1b}
.rights{position:absolute;left:36px;top:306px;font-size:13px}
.badges{position:absolute;left:330px;top:262px;display:flex;gap:18px;align-items:center}
.badge{width:64px;height:62px;background:rgba(255,255,255,.85)}
.badge.round{border-radius:50%;background:#b8a48a}
.badge.dark{background:#2d3553}
.badge.red{background:#c9313b}
.badge.pill{width:100px;height:38px;border-radius:19px;background:var(--white)}
</style>
</head>
<body>

<header class="hero">
  <div class="brand"><span class="brand-dot"></span><span class="brand-name">Veldon</span></div>
  <div class="lang">English</div>
  <nav class="nav">
    <a class="active">Home</a>
    <a class="drop">Solution</a>
    <a>Pricing</a>
    <a class="drop">Resources</a>
    <a class="drop">About</a>
  </nav>
  <div class="awards">
    <div class="award">
      <svg width="24" height="24" viewBox="0 0 24 24"><path d="M6 3h12v5a6 6 0 0 1-12 0z M3 4h3v3a3 3 0 0 1-3-3z M18 4h3a3 3 0 0 1-3 3z M10 14h4v4h3v3H7v-3h3z" fill="#fff"/></svg>
      <span>In 2020, VELDON won the Cyber Security<br>Excellence Award for Best "Anti Phishing"</span>
    </div>
    <div class="award">
      <svg width="28" height="28" viewBox="0 0 28 28"><circle cx="14" cy="14" r="11" fill="none" stroke="#fff" stroke-width="2" stroke-dasharray="4 3"/><path d="M14 8l2 4 4 .5-3 3 .8 4-3.8-2-3.8 2 .8-4-3-3 4-.5z" fill="#fff"/></svg>
      <span>In 2020, VELDON won the Cyber Security Excellence<br>Award for Best "Security Education Platform".</span>
    </div>
    <div class="award">
      <svg width="28" height="28" viewBox="0 0 28 28"><circle cx="14" cy="14" r="11" fill="none" stroke="#fff" stroke-width="2" stroke-dasharray="4 3"/><text x="14" y="19" font-size="13" fill="#fff" text-anchor="middle" font-family="Montserrat,sans-serif">1</text></svg>
      <span>2020 Gold Winner "Cyber Security Education<br>and Training" in the Security Product Review</span>
    </div>
  </div>

  <div class="eyebrow">CYBER SECURITY STARTS WITH PEOPLE</div>
  <h1 class="hero-title">TRAIN YOUR STAFF WITH<br>VELDON AND IMPROVE CYBER<br>SECURITY AWARENESS</h1>
  <div class="demo-btn">Request a demo</div>
  <div class="hero-illus" role="img" aria-label="Illustration of two staff members beside a monitor with a security shield, keys, padlocks and clouds"></div>
  <div class="dots"><span></span><span></span></div>
</header>

<section class="help">
  <h2>HOW CAN WE HELP?</h2>

  <article class="card" style="left:46px">
    <h3 style="top:52px">IMPORT OUR TRAINING<br>COURSES IN YOUR LMS</h3>
    <p class="lead" style="top:112px;font-size:14px;line-height:17px">Buy out of the box or custom tailored security courses you can import in your elearning (SCORM)</p>
    <p class="body" style="top:184px">VELDON offers 250 fully customizable training modules in +30 languages. Games, videos, exams, posters, offline, micro-training and much more!</p>
    <div class="card-btn" style="left:28px;top:310px;width:234px">EXPLORE OUR TRAINING</div>
  </article>

  <article class="card" style="left:359px">
    <h3 style="top:52px">LET US DEVELOP A SECURITY<br>AWARENESS PROGRAM</h3>
    <p class="lead" style="top:104px">VELDON Security will assist you in improving security awareness - with money back guarantee!</p>
    <p class="body" style="top:184px;font-size:15px;line-height:19.5px">Our security awareness specialists will identify risky users via phishing simulations. We develop a tailored awareness program and reduce your exposure to social hacking.</p>
    <div class="card-btn" style="left:29px;top:308px;width:231px">EXPLORE OUR SERVICES</div>
  </article>

  <article class="card" style="left:672px">
    <h3 style="top:44px;left:14px">INSTALL THE VELDON SOFTWARE<br>ON-PREMISE OR GET ACCESS<br>TO THE SAAS VERSION</h3>
    <p class="lead" style="top:120px;left:14px">You want to run the campaign yourself? Choose your prefered setup type and get started in 24h!</p>
    <p class="body" style="top:212px;left:12px;font-size:14.5px;line-height:19px">The VELDON software can be installed on-premise or in the cloud. If you don't want to deal with the installation we onboard you in 24 h on our SaaS!</p>
    <div class="card-btn" style="left:18px;top:308px;width:234px">EXPLORE OUR SOFTWARE</div>
  </article>
</section>

<section class="mssp">VELDON is also available for MSSP -<a>Learn More</a></section>

<section>
  <h2 class="trust-title" style="font-weight:400">Already over <span class="num">12'000'000</span><br>Employees worldwide trust and use VELDON.</h2>
  <div class="trust-copy">
    <p>Veldon Guard is a name you can trust! Because we have won countless awards since 2015 and help well-known brands around the world.</p>
    <p>You know you're getting a quality solution with us.</p>
    <p>Our services can be customized to fit your needs and company size. Talk to our team today to learn more.</p>
  </div>
  <div class="cta">GET IN CONTACT WITH THE VELDON TEAM NOW!</div>

  <div class="clients">
    <div class="client" style="left:15px;top:50px;color:#1d3f8f">Norvia</div>
    <div class="client" style="left:115px;top:50px;color:#d7252b">Railox</div>
    <div class="client" style="left:225px;top:50px;color:#d7252b;font-size:17px">Hausmond</div>
    <div class="client" style="left:15px;top:126px;color:#d7252b"><span class="sq"></span>Kessler</div>
    <div class="client" style="left:150px;top:126px;color:#1d3f8f">Alpenflug</div>
    <div class="client" style="left:15px;top:198px;color:#1d3f8f">Mühlberg</div>
    <div class="client" style="left:176px;top:190px;color:#5a6fb8;font-weight:500;font-size:14px;line-height:16px">Falkner<br>Informatik</div>
    <div class="client" style="left:15px;top:265px;color:#222">Chemora</div>
    <div class="client" style="left:176px;top:258px;color:#333;font-weight:500;font-size:14px;line-height:16px">Stadtwerk<br>Nord</div>
  </div>
</section>

<footer class="footer">
  <div class="frame"></div>
  <div class="abs" style="left:77px;top:19px"><h4>CONTACTS</h4></div>
  <div class="abs" style="left:77px;top:60px">Address: Europe<br>Veldon Guard AG<br>Seefeldweg 12 | 6005 Lucerne | Switzerland</div>
  <div class="abs" style="left:435px;top:40px">Address: North America<br>Veldon Guard USA<br>4410 Harbor Point Rd<br>Suite 210<br>Denver, CO 80202</div>
  <div class="abs" style="left:690px;top:44px">Phone Global: +41 44 000 12 34<br>Phone USA: +1-555-010-2200<br>Phone USA Support: +1-555-010-2214<br>Phone France: +33 600 010 200<br>Phone UK: +44 (0) 7700 900123</div>
  <div class="abs" style="left:1019px;top:19px"><h4>LANGUAGE</h4></div>
  <div class="abs lang" style="left:1019px;top:56px;font-size:13px">English</div>
  <div class="rule"></div>
  <div class="foot-brand"><span class="brand-dot"></span><span class="n">Veldon</span></div>
  <div class="rights">All Rights Reserved 2020</div>
  <div class="badges">
    <div class="badge" style="background:#f0a14a"></div>
    <div class="badge round"></div>
    <div class="badge dark" style="width:48px"></div>
    <div class="badge red" style="width:50px"></div>
    <div class="badge red" style="width:48px"></div>
    <div class="badge" style="width:70px;height:34px"></div>
    <div class="badge red" style="width:50px;background:#e0452f"></div>
    <div class="badge dark" style="width:62px"></div>
    <div class="badge pill"></div>
    <div class="badge round" style="background:#ffffff;border:3px solid #2a6fd0"></div>
  </div>
</footer>

</body>
</html>
```